" A proprietária é a Lorena Bastolli, Biomedica, pós graduada em estética e Mestra pela Universidade de Vale Dourado. Temos trabalhando conosco uma fisioterapeuta, uma esteticista, uma estagiária em biomedica, uma secretária, e temos parceria com uma Nutricionista com PHD e uma Médica especialista em Endocrinologia, ambas atendem na clínica uma vez por semana. "

```html
<!DOCTYPE html>
<html lang="pt-BR">
<head>
<meta charset="utf-8">
<title>Lorena Bastolli — Papelaria</title>
<link rel="stylesheet" href="https://fonts.googleapis.com/css2?family=Cormorant+Garamond:wght@500;600&family=Montserrat:wght@400;500&display=swap">
<style>
  :root {
    --backdrop: #e6e6e4;
    --paper: #ffffff;
    --ink: #2f2f31;
    --ink-soft: #6b6b6e;
    --gold: #c9a368;
    --pattern: #f1f1f2;
    --card-dark: #3b3b3e;
    --card-dark-pattern: #434347;
    --shadow: rgba(0,0,0,0.14);
  }
  * { box-sizing: border-box; margin: 0; padding: 0; }
  html, body { width: 1200px; height: 1200px; overflow: hidden; }
  body {
    background: var(--backdrop);
    font-family: "Montserrat", sans-serif;
    color: var(--ink);
    position: relative;
  }
  .serif { font-family: "Cormorant Garamond", serif; }

  /* Letterhead */
  .letterhead {
    position: absolute;
    left: 470px; top: 140px;
    width: 636px; height: 900px;
    background: var(--paper);
    box-shadow: 0 8px 30px var(--shadow);
  }
  .letterhead__pattern-top {
    position: absolute; left: 36px; top: 36px;
    width: 530px; height: 46px;
    background: linear-gradient(90deg, rgba(241,241,242,0) 0%, var(--pattern) 40%);
  }
  .letterhead__pattern-side {
    position: absolute; right: 24px; top: 36px;
    width: 46px; height: 640px;
    background: linear-gradient(180deg, var(--pattern) 60%, rgba(241,241,242,0) 100%);
  }
  .letterhead__mark {
    position: absolute; right: 34px; top: 28px;
    width: 28px; height: 28px; border-radius: 50%;
    background: var(--gold);
  }
  .letterhead__contacts {
    position: absolute; left: 48px; bottom: 44px;
    list-style: none;
    font-size: 10px; line-height: 20px; color: var(--ink-soft);
  }
  .letterhead__contacts li { display: flex; align-items: center; gap: 8px; }
  .letterhead__contacts svg { width: 10px; height: 10px; fill: var(--gold); }
  .letterhead__name {
    position: absolute; right: 48px; bottom: 112px;
    text-align: right;
    font-size: 30px; line-height: 28px; font-weight: 600;
    color: var(--ink);
  }

  /* Business cards */
  .card {
    position: absolute;
    width: 380px; height: 216px;
    box-shadow: 0 6px 20px var(--shadow);
  }
  .card--front {
    left: 60px; top: 380px;
    background: var(--paper);
    padding: 34px 28px;
  }
  .card--front .card__mark {
    width: 20px; height: 20px; border-radius: 50%; background: var(--gold);
    margin-bottom: 12px;
  }
  .card__name { font-size: 20px; font-weight: 600; color: var(--ink); }
  .card__role { font-size: 10px; color: var(--gold); letter-spacing: 0.5px; margin-top: 2px; }
  .card__contacts {
    position: absolute; right: 26px; top: 90px;
    list-style: none; font-size: 9px; line-height: 17px; color: var(--ink-soft);
    text-align: right;
  }
  .card__address {
    position: absolute; left: 28px; bottom: 26px;
    font-size: 9px; line-height: 14px; color: var(--ink-soft);
  }
  .card__pattern-strip {
    position: absolute; left: 28px; right: 26px; top: 16px; height: 10px;
    background: var(--pattern);
  }

  .card--back {
    left: 60px; top: 640px;
    background: var(--card-dark);
    display: flex; align-items: center; justify-content: center; gap: 14px;
  }
  .card--back .card__pattern {
    position: absolute; inset: 0;
    background: radial-gradient(circle at 50% 50%, var(--card-dark-pattern) 0%, var(--card-dark) 75%);
  }
  .card--back .card__mark {
    position: relative;
    width: 26px; height: 26px; border-radius: 50%; background: var(--gold);
  }
  .card--back .card__name {
    position: relative;
    color: #ffffff; font-size: 26px; line-height: 24px;
  }
</style>
</head>
<body>

  <section class="card card--front" aria-label="Cartão de visita, frente">
    <div class="card__pattern-strip" role="img" aria-label="Faixa de padrão floral suave"></div>
    <div class="card__mark"></div>
    <p class="card__name serif">Lorena Bastolli</p>
    <p class="card__role">Biomédica Esteta</p>
    <ul class="card__contacts">
      <li>+55 (16) 3721-0480</li>
      <li>contato@lorenabastolli.com.br</li>
      <li>www.lorenabastolli.com.br</li>
    </ul>
    <p class="card__address">R. das Acácias, 412<br>Vale Dourado - SP</p>
  </section>

  <section class="card card--back" aria-label="Cartão de visita, verso">
    <div class="card__pattern" role="img" aria-label="Padrão floral tom sobre tom"></div>
    <div class="card__mark"></div>
    <p class="card__name serif">Lorena<br>Bastolli</p>
  </section>

  <section class="letterhead" aria-label="Papel timbrado">
    <div class="letterhead__pattern-top" role="img" aria-label="Borda de padrão floral suave"></div>
    <div class="letterhead__pattern-side" role="img" aria-label="Borda de padrão floral suave"></div>
    <div class="letterhead__mark"></div>

    <ul class="letterhead__contacts">
      <li><svg viewBox="0 0 10 10"><path d="M2 0h2l1 2.5-1.3 1a5 5 0 0 0 2.8 2.8l1-1.3L10 6v2c0 1-1 2-2 2A8 8 0 0 1 0 2c0-1 1-2 2-2z"/></svg>+55 (16) 3721-0480</li>
      <li><svg viewBox="0 0 10 10"><path d="M5 0a3.5 3.5 0 0 1 3.5 3.5C8.5 6 5 10 5 10S1.5 6 1.5 3.5A3.5 3.5 0 0 1 5 0zm0 2a1.5 1.5 0 1 0 0 3 1.5 1.5 0 0 0 0-3z"/></svg>R. das Acácias, 412 - Vale Dourado - SP</li>
      <li><svg viewBox="0 0 10 10"><path d="M0 2h10v6H0zM0 2l5 3.5L10 2" stroke="#fff" stroke-width="0.8"/></svg>contato@lorenabastolli.com.br</li>
      <li><svg viewBox="0 0 10 10"><circle cx="5" cy="5" r="4.5"/></svg>www.lorenabastolli.com.br</li>
    </ul>

    <p class="letterhead__name serif">Lorena<br>Bastolli</p>
  </section>

</body>
</html>
```